Corrimal Lodge Web Design Project

I am looking for a striking, modern and user friendly site to promote my business, Corrimal Lodge.

Corrimal Lodge comprises of 3 elements : Restaurant, Resort and Events and the site must showcase all of these.
Updates

Project Deadline Extended
Reason: Too far away from brief ! Please check out the 2 website links to restaurant sites i LOVE for inspiration ! I am happy to pay for a quality designer and also for anyone that can code this !

Target Market(s)

Our Restaurant clientele demographic is 30-60 years old and are a mix of locals and tourists. The Restaurant is very much a destination venue so we attract people that wish to seek out amazing food.

The Event side of things attracts mainly weddings, this is a lucrative arm of the business and this side of the site must also be outstanding.

The Resort comprises of 7 boutique loft apartment and has a big pool and spa. We attract a mix of locals but want to push it as a ' getaway '

Industry/Entity Type

Business

Requirements
Must have
• I would like the first page to be an overall blog and to highlight the 3 area of the business. Lets have the 3 keywords as clickable tabs that take you to that section of the site.

RESTAURANT RESORT EVENTS

The RESTAURANT page should include the following tabs ( i have provided the information to be added to each tab as an example )

MENU ( Breakfast, Lunch, Dinner, Set Menu, Wine List)

FUNCTIONS (Private Dining Room, Exclusive Use, Wine Nights Coming Soon)

RESERVATIONS (Enquiry Form linked to my info@ address, Reservation Policies, Contact Number)

GALLERY & PRESS ( Press Articles, Latest News, What's On, Photo's, Wedding Hot Spot)

CONTACT US (Opening Times, Map, Contact Details, Sign Up For Our Newsletter, Facebook Link )

The RESORT page should include the following tabs :
# LOFTS & RATES
# FACILITIES
# SPECIAL OFFERS
# GALLERY
# RESERVATIONS

The EVENTS page should include the following tabs :
# WEDDINGS
# CONFERENCES
# PRIVATE EVENTS
# GALLERY
# ENQUIRY FORM
Nice to have
• Include Logo, good branding

```html
<!DOCTYPE html>
<html lang="en">
<head>
<meta charset="utf-8">
<title>Corrimal Lodge</title>
<link rel="stylesheet" href="https://fonts.googleapis.com/css2?family=Fondamento&display=swap">
<style>
  :root {
    --wood-light: #d9a86b;
    --wood-mid: #c48a4c;
    --wood-dark: #9c6431;
    --brand-red: #8a1014;
    --brand-red-dark: #5e0709;
    --ink-light: #ffffff;
    --footer-ink: #ffffff;
  }
  html, body {
    margin: 0;
    padding: 0;
    overflow: hidden;
  }
  .page {
    position: relative;
    width: 1200px;
    height: 1200px;
    overflow: hidden;
    font-family: "Fondamento", Georgia, serif;
  }
  .wood-floor {
    position: absolute;
    inset: 0;
    background:
      radial-gradient(ellipse at 50% 45%, rgba(255,230,180,0.35), rgba(0,0,0,0) 60%),
      linear-gradient(90deg, var(--wood-mid), var(--wood-light) 30%, var(--wood-mid) 55%, var(--wood-light) 75%, var(--wood-dark));
  }
  .site-title {
    position: absolute;
    left: 265px;
    top: 60px;
    width: 505px;
    height: 75px;
    border-radius: 50%;
    background: radial-gradient(ellipse at 50% 40%, var(--brand-red), var(--brand-red-dark));
    box-shadow: 0 4px 10px rgba(0,0,0,0.45);
    display: flex;
    align-items: center;
    justify-content: center;
    margin: 0;
    color: var(--ink-light);
    font-weight: 400;
    font-size: 42px;
    letter-spacing: 1px;
  }
  .brand-mark {
    position: absolute;
    right: 40px;
    top: 18px;
    width: 130px;
    display: flex;
    flex-direction: column;
    align-items: center;
    gap: 8px;
  }
  .brand-mark__square {
    width: 64px;
    height: 64px;
    border: 3px solid var(--ink-light);
    box-sizing: border-box;
  }
  .brand-mark__name {
    color: var(--ink-light);
    font-size: 17px;
    white-space: nowrap;
  }
  .social-link {
    position: absolute;
    left: 1071px;
    width: 66px;
    height: 66px;
    border-radius: 50%;
    background: var(--ink-light);
    box-shadow: 0 2px 6px rgba(0,0,0,0.35);
  }
  .social-link--first { top: 144px; }
  .social-link--second { top: 241px; }
  .section-card {
    position: absolute;
    width: 306px;
    height: 258px;
    background: var(--brand-red);
    border-radius: 9px;
    box-shadow: 4px 8px 14px rgba(0,0,0,0.55);
    text-decoration: none;
  }
  .section-card__title {
    position: absolute;
    left: 0;
    right: 0;
    top: 6px;
    text-align: center;
    color: var(--ink-light);
    font-size: 44px;
    line-height: 56px;
    margin: 0;
    font-weight: 400;
  }
  .section-card__photo {
    position: absolute;
    left: 21px;
    top: 73px;
    width: 264px;
    height: 175px;
  }
  .section-card--restaurant { left: 387px; top: 245px; height: 260px; }
  .section-card--resort { left: 621px; top: 528px; }
  .section-card--events { left: 291px; top: 749px; }
  .photo--restaurant {
    background: linear-gradient(180deg, #d8d2c2 0%, #a98a5f 40%, #6e4b2c 70%, #e6e3dc 100%);
  }
  .photo--resort {
    background: linear-gradient(180deg, #4f8fd6 0%, #c98f4a 35%, #6b8a3e 60%, #2aa5d9 80%, #3b7d3a 100%);
  }
  .photo--events {
    background: linear-gradient(180deg, #b7c8d6 0%, #3f6b3a 45%, #4f8a3a 70%, #e9ece6 100%);
  }
  .site-footer {
    position: absolute;
    left: 0;
    right: 0;
    top: 1158px;
    font-family: Arial, Helvetica, sans-serif;
    color: var(--footer-ink);
    font-size: 20px;
  }
  .site-footer__copyright { position: absolute; left: 252px; }
  .site-footer__privacy {
    position: absolute;
    left: 754px;
    font-size: 22px;
    color: var(--footer-ink);
    text-decoration: none;
  }
</style>
</head>
<body>
<div class="page">
  <div class="wood-floor" role="img" aria-label="Warm timber floorboard background"></div>

  <h1 class="site-title">Corrimal Lodge</h1>

  <div class="brand-mark">
    <div class="brand-mark__square"></div>
    <span class="brand-mark__name">Corrimal Lodge</span>
  </div>

  <a class="social-link social-link--first" href="#" aria-label="Social page"></a>
  <a class="social-link social-link--second" href="#" aria-label="Social feed"></a>

  <a class="section-card section-card--restaurant" href="#restaurant">
    <h2 class="section-card__title">Restaurant</h2>
    <div class="section-card__photo photo--restaurant" role="img" aria-label="Elegant dining room with round tables set in white linen"></div>
  </a>

  <a class="section-card section-card--resort" href="#resort">
    <h2 class="section-card__title">Resort</h2>
    <div class="section-card__photo photo--resort" role="img" aria-label="Loft apartments beside a blue pool with palm trees"></div>
  </a>

  <a class="section-card section-card--events" href="#events">
    <h2 class="section-card__title">Events</h2>
    <div class="section-card__photo photo--events" role="img" aria-label="Outdoor wedding reception on a lawn overlooking the water"></div>
  </a>

  <footer class="site-footer">
    <span class="site-footer__copyright">copyright Corrimal Lodge 2013</span>
    <a class="site-footer__privacy" href="#privacy">Privacy Policy</a>
  </footer>
</div>
</body>
</html>
```